Tender Wedded Hours podcast website redesign

Simple podcast website. Might be similar to lumiqua.com (I own this website too so no copyright issues) but I'd like to see fresh ideas too. Here's another simple site that I like: https://vendira.com/

I just need to be able to move all my podcasts over to this website and it not to break anything... I've had a couple of web developers work on it and it needs some work.

I'm not sure how things work on the backend, but the website needs to be able to move all the info from www.tenderweddedhours.com onto the new webdesign of this project.

Target Market(s)

wives

Number of Pages Required

4 page

Font styles to use
Sans Serif
Script

Colors
fdf0f6
f9d9e8
fee3d4

Requirements
Must have
• Simple (example: https://dovrenkell.com/)
• Lovely (example: lumiqua.com)
• A post page, where posts will show up and show a bit about the podcast (like: http://lumiqua.com/podcasts/
• On posts I need a podcast audio plugin the post needs to have the audio-bar at the top: https://merivontrack.com/
• I'd really like a lot of space
• Gorgeous mobile (example: https://dovrenkell.com/ looks fantastic in mobile and I really like how it centers and theres a lot of space around in desktop)
• And just as gorgeous desktop
• It should be very easy to change on backend.
Nice to have
• Mostly white space, with some pastels and then black writing. I'd be curious if you have other ideas to "up market" the look. Also, I've attached my current podcast logo, but that is subject to change if the website seems to necessitate it.
Should not have
• Should not be busy. Very simple and elegant and upmarket.

```html
<!DOCTYPE html>
<html lang="en">
<head>
<meta charset="utf-8">
<title>Tender Wedded Hours — Podcast</title>
<link rel="stylesheet" href="https://fonts.googleapis.com/css2?family=Montserrat:wght@400;500;600;700;800&family=Open+Sans:wght@400;600&family=Dancing+Script:wght@600;700&display=swap">
<style>
:root{
  --pink:#ee4c7c;
  --pink-deep:#d93a68;
  --blush:#fdf0f6;
  --rose:#f9d9e8;
  --peach:#fee3d4;
  --ink:#1f1f24;
  --text:#55555c;
  --muted:#9a9aa2;
  --line:#e6e6ea;
  --grey:#f3f3f4;
  --white:#ffffff;
}
*{box-sizing:border-box;margin:0;padding:0}
html,body{width:1200px;height:2728px;overflow:hidden}
body{background:var(--white);font-family:"Open Sans",Arial,sans-serif;color:var(--text);position:relative}
.sans{font-family:"Montserrat",Arial,sans-serif}
.script{font-family:"Dancing Script",cursive}
.brand{font-family:"Montserrat",Arial,sans-serif;font-weight:800;color:var(--pink);text-transform:uppercase;letter-spacing:.5px;display:flex;align-items:center;gap:8px}
.brand .dot{width:12px;height:12px;border-radius:50%;background:var(--pink)}

/* header */
.site-header{position:absolute;top:0;left:0;width:1200px;height:58px;display:flex;align-items:center;padding:0 230px;justify-content:space-between}
.site-header .brand{font-size:15px;line-height:1.05;width:120px}
.nav{display:flex;gap:18px;font-family:"Montserrat",Arial,sans-serif;font-size:10px;font-weight:600;color:var(--ink)}
.socials{display:flex;gap:9px}
.socials span{width:9px;height:9px;border-radius:50%;background:var(--ink)}
.btn{display:inline-flex;align-items:center;justify-content:center;font-family:"Montserrat",Arial,sans-serif;font-weight:700;font-size:11px;letter-spacing:1px;text-transform:uppercase;border-radius:20px}
.btn-fill{background:var(--pink);color:var(--white)}
.btn-line{border:2px solid var(--pink);color:var(--pink);background:var(--white)}
.site-header .btn{width:110px;height:26px;font-size:9px}

/* hero */
.hero{position:absolute;top:58px;left:0;width:1200px;height:400px;background:linear-gradient(90deg,#f7c7d8 0%,#f9d9e8 55%,#fdeef4 100%)}
.hero-photo{position:absolute;right:210px;top:0;width:340px;height:400px;background:linear-gradient(180deg,#f3cfdc,#e9b9c9 60%,#d8a3b6)}
.hero-copy{position:absolute;left:230px;top:72px;width:440px}
.hero h1{font-family:"Montserrat",Arial,sans-serif;font-weight:800;color:var(--pink-deep);font-size:30px;line-height:1.1}
.hero .sub{font-family:"Montserrat",Arial,sans-serif;font-weight:700;font-size:12px;color:var(--ink);margin-top:10px;letter-spacing:.5px}
.hero-player{margin-top:20px;display:flex;align-items:center;gap:10px}
.play{width:26px;height:26px;background:var(--pink);border-radius:3px;display:flex;align-items:center;justify-content:center}
.track{flex:1;height:3px;background:rgba(255,255,255,.8);position:relative}
.track i{position:absolute;left:0;top:0;height:3px;width:35%;background:var(--pink)}
.time{font-size:9px;color:var(--ink)}
.hero-actions{margin-top:48px;display:flex;gap:14px}
.hero-actions .btn{width:104px;height:34px;border-radius:3px;font-size:10px}

/* intro */
.intro{position:absolute;top:488px;left:230px;width:740px;height:230px}
.portrait{position:absolute;left:0;top:0;width:92px;height:92px;border-radius:50%;background:linear-gradient(160deg,#c79a6e,#8c6c58)}
.intro-text{position:absolute;left:120px;top:0;width:620px;font-size:9.5px;line-height:1.6}
.intro-text p{margin-bottom:10px}
.signature{position:absolute;right:0;top:188px;font-size:30px;color:var(--ink)}

/* award band */
.award{position:absolute;top:736px;left:0;width:1200px;height:400px;background:var(--grey);text-align:center}
.medal{margin:38px auto 0;width:40px;height:54px}
.award p{width:740px;margin:26px auto 0;text-align:left;font-size:22px;line-height:1.5;color:var(--ink)}
.award .brand{justify-content:center;font-size:22px;margin-top:26px;line-height:1.05}
.award .brand b{display:block;text-align:center}

/* podcasts */
.podcasts{position:absolute;top:1140px;left:230px;width:740px}
.section-title{text-align:center;font-size:36px;color:var(--ink);font-weight:700}
.episode{display:flex;gap:22px;margin-top:32px;align-items:center}
.episode:first-of-type{margin-top:30px}
.cover{width:150px;height:150px;flex:none}
.ep-body{flex:1}
.ep-title{font-family:"Montserrat",Arial,sans-serif;font-size:10px;font-weight:700;color:var(--ink)}
.ep-desc{font-size:8.5px;margin-top:8px;color:var(--muted)}
.ep-player{margin-top:28px;display:flex;align-items:center;gap:10px;font-size:8px;color:var(--ink)}
.ep-player .track{background:var(--line)}
.ep-player .track i{width:0}
.vol{width:40px;height:3px;background:var(--ink)}
.more{display:flex;justify-content:center;margin-top:40px}
.more .btn{width:130px;height:34px;border-radius:3px;font-size:9px}

/* testimonial */
.testimonial{position:absolute;top:1830px;left:230px;width:740px;height:280px}
.testimonial .section-title{text-align:left;font-size:30px}
.quote-card{position:absolute;left:0;top:56px;width:360px;height:200px;background:var(--white);box-shadow:0 4px 18px rgba(0,0,0,.08);padding:24px 26px}
.quote-card h4{font-family:"Montserrat",Arial,sans-serif;font-size:10px;font-weight:700;color:var(--ink)}
.quote-card p{font-size:8.5px;line-height:1.6;margin-top:10px}
.quote-card .who{position:absolute;right:26px;bottom:20px;font-size:9px;color:var(--ink)}
.quote-mark{position:absolute;left:-8px;top:-14px;font-family:"Montserrat",Arial,sans-serif;font-size:50px;color:var(--pink);font-weight:800;line-height:1}
.video{position:absolute;right:0;top:10px;width:360px;height:236px;background:linear-gradient(135deg,#a9b7c4,#6f7f8e 55%,#4c5864)}
.video .playbtn{position:absolute;left:154px;top:94px;width:52px;height:36px;border-radius:8px;background:rgba(0,0,0,.6);display:flex;align-items:center;justify-content:center}

/* our ladies */
.ladies{position:absolute;top:2132px;left:0;width:1200px;height:430px;background:linear-gradient(180deg,#f3a7bf,#f0b7c9 55%,#f6cbd8)}
.ladies .section-title{color:var(--white);padding-top:30px;font-size:34px}
.ladies .lead{text-align:center;color:var(--white);font-family:"Dancing Script",cursive;font-size:17px;margin-top:4px}
.form{width:360px;margin:30px auto 0}
.field{height:28px;background:var(--white);border-radius:2px;margin-bottom:12px}
.row{display:flex;gap:12px}
.row .field{flex:1}
.area{height:80px}
.send{display:flex;justify-content:center;margin-top:12px}
.send .btn{width:74px;height:26px;border-radius:3px;font-size:9px}

/* footer */
.site-footer{position:absolute;top:2562px;left:0;width:1200px;height:166px;background:var(--white)}
.contact{position:absolute;left:230px;top:40px;display:flex;gap:40px;font-size:8.5px;color:var(--ink)}
.contact div{display:flex;align-items:center;gap:8px}
.site-footer .brand{position:absolute;left:540px;top:30px;font-size:15px;line-height:1.05;width:140px}
.site-footer .socials{position:absolute;right:230px;top:44px}
.copy{position:absolute;right:230px;top:74px;font-size:7.5px;color:var(--muted)}
</style>
</head>
<body>

<header class="site-header">
  <div class="brand"><span>Tender<br>Wedded Hours</span></div>
  <nav class="nav"><span>About Me</span><span>Podcasts</span><span>Resources</span><span>Products</span><span>Contact</span><span>My Checklist</span></nav>
  <div class="socials"><span></span><span></span><span></span><span></span><span></span></div>
  <a class="btn btn-fill">Subscribe Now</a>
</header>

<section class="hero">
  <div class="hero-photo" role="img" aria-label="Smiling couple standing back to back"></div>
  <div class="hero-copy">
    <h1>THE BEST PLAYER FOR<br>SERIOUS PODCASTERS</h1>
    <div class="sub">MY BROTHER WAS FOUND WITHOUT A PULSE...</div>
    <div class="hero-player">
      <div class="play"><svg width="10" height="10" viewBox="0 0 10 10"><path d="M2 1l7 4-7 4z" fill="#fff"/></svg></div>
      <span class="time">00:00</span>
      <div class="track"><i></i></div>
      <span class="time">32:14</span>
    </div>
    <div class="hero-actions"><a class="btn btn-line">Learn More</a><a class="btn btn-fill">Get Started</a></div>
  </div>
</section>

<section class="intro">
  <div class="portrait" role="img" aria-label="Portrait of the podcast host"></div>
  <div class="intro-text">
    <p>It's hard to feel all in when a good marriage starts slipping. Hi there, I'm Marla. Welcome, and I'm so glad you found this space. You are not alone here.</p>
    <p>Tender Wedded Hours is about giving you warm tools to love your husband well. Each episode is short, honest and easy to use in daily life, so you can build the closeness you both want.</p>
    <p>If you have ever felt unseen, tired or unsure where to begin, this show is for you. We talk about friendship, romance, desire and faith, with kind words and clear steps that help you grow each week.</p>
    <p>Let's do this together. Press play, pour some tea, and let's make your home a place of rest and joy again.</p>
  </div>
  <div class="signature script">Marla Vey</div>
</section>

<section class="award">
  <svg class="medal" viewBox="0 0 40 54"><path d="M10 0h8l4 14h-8zM30 0h-8l-4 14h8z" fill="#c93a3a"/><circle cx="20" cy="34" r="18" fill="#d9a63a"/><circle cx="20" cy="34" r="12" fill="#e9c15b"/></svg>
  <p>Marla Vey is a marriage and intimacy expert and coach. Her podcast was awarded 19th of the Top 30 Relationship podcasts and she is passionate about helping you have incredible intimacy and joy in your relationship!</p>
  <div class="brand"><b>Tender<br>Wedded Hours</b></div>
</section>

<section class="podcasts">
  <h2 class="section-title script">Our Podcasts</h2>
  <article class="episode">
    <div class="cover" role="img" aria-label="Episode cover art with soft forest tones" style="background:linear-gradient(135deg,#8a8a5a,#5d6a3e)"></div>
    <div class="ep-body">
      <div class="ep-title">♪ 178 Should you tell her about your past sex life?</div>
      <div class="ep-desc">An honest look at what to share and when to share it.</div>
      <div class="ep-player"><svg width="8" height="8" viewBox="0 0 10 10"><path d="M2 1l7 4-7 4z" fill="#1f1f24"/></svg><span>00:00</span><div class="track"><i></i></div><span>28:40</span><div class="vol"></div></div>
    </div>
  </article>
  <article class="episode">
    <div class="cover" role="img" aria-label="Episode cover art with pale blue tones" style="background:linear-gradient(135deg,#9fb6c4,#6d8797)"></div>
    <div class="ep-body">
      <div class="ep-title">♪ 177 Last week, My brother was found without a pulse</div>
      <div class="ep-desc">A hard week, and what it taught me about love.</div>
      <div class="ep-player"><svg width="8" height="8" viewBox="0 0 10 10"><path d="M2 1l7 4-7 4z" fill="#1f1f24"/></svg><span>00:00</span><div class="track"><i></i></div><span>31:05</span><div class="vol"></div></div>
    </div>
  </article>
  <div class="more"><a class="btn btn-fill">Browse More</a></div>
</section>

<section class="testimonial">
  <h2 class="section-title script">Testimonial</h2>
  <div class="quote-card">
    <span class="quote-mark">“</span>
    <h4>JANE, JUST MARRIED</h4>
    <p>Each episode feels like a talk with a wise friend. I have learned to listen more, laugh more and open my heart to my husband again. Our home feels calmer and so much closer. I am so thankful for this show.</p>
    <span class="who">— Jane</span>
  </div>
  <div class="video" role="img" aria-label="Video still of the host speaking into a microphone">
    <div class="playbtn"><svg width="14" height="14" viewBox="0 0 10 10"><path d="M2 1l7 4-7 4z" fill="#fff"/></svg></div>
  </div>
</section>

<section class="ladies">
  <h2 class="section-title script">Our Ladies</h2>
  <div class="lead">Sign up for encouragement and inspiration to grow an intentional marriage!</div>
  <div class="form">
    <div class="row"><div class="field"></div><div class="field"></div></div>
    <div class="field"></div>
    <div class="field area"></div>
    <div class="send"><a class="btn btn-fill">Send</a></div>
  </div>
</section>

<footer class="site-footer">
  <div class="contact">
    <div><svg width="14" height="14" viewBox="0 0 24 24"><path d="M6.6 10.8a15 15 0 006.6 6.6l2.2-2.2a1 1 0 011-.25 11 11 0 003.5.56 1 1 0 011 1V20a1 1 0 01-1 1A17 17 0 013 4a1 1 0 011-1h3.5a1 1 0 011 1 11 11 0 00.56 3.5 1 1 0 01-.25 1z" fill="#ee4c7c"/></svg><span>Call Us<br>(555) 014-2290</span></div>
    <div><svg width="14" height="14" viewBox="0 0 24 24"><rect x="2" y="5" width="20" height="14" rx="2" fill="#ee4c7c"/><path d="M3 6l9 7 9-7" stroke="#fff" stroke-width="1.6" fill="none"/></svg><span>Email<br>hello@tenderweddedhours.com</span></div>
  </div>
  <div class="brand"><span>Tender<br>Wedded Hours</span></div>
  <div class="socials"><span></span><span></span><span></span><span></span><span></span></div>
  <div class="copy">Copyright © 2019 Tender Wedded Hours. All Rights Reserved.</div>
</footer>

</body>
</html>
```